Mutig voran
Wir sind richtig begeistert von dieser Möglichkeit, in kurzer Zeit einen guten Entwurf zu erhalten und auch mitgestalten zu können. Vor allem die Auswahl aus verschiedenen Vorschlägen hat unseren eigenen Blick für das geschärft, was wir wollten. Vielen Dank. Es wird sicher nicht das letzte Mal sein, dass wir diese Möglichkeit nutzen.
Zielgruppe
Zielgruppe sind junge Eltern im Stadtteil Richtsberg in Marburg, einem multikulturellen Stadtteil. Die Stadtteilhebamme begleitet junge Familien am Richtsberg vor und nach der Geburt in den ersten Lebensjahren, die VKM (Nachbarschaftsbund für offene Wege e.V.) ist ein Gemeinwesenprojekt die im Stadtteil Anlaufstelle für Stadtteilbewohner, die Beratungsstellen Wendelhof bestehen aus einer Psychologischen Beratungsstelle mit Erziehungsberatung und einer Schwangerenberatungsstelle (in der Stadt)
Aufgabenstellung
Der Text wird als Datei übermittelt, es soll ein Plakat erstellt werden, das
a) die Kooperation der Beteiligten vermittelt
b) das Angebot nahebringt
c) die Kontaktaufnahme ermöglicht
Das Plakat sollte möglichst auch in verkleinerter Form (Din A5?) gedruckt werden können
Das Logo für die VKM ist als Datei angehängt,
das Logo für die Beratungsstellen ist in drei verschiedenen Dateiformaten angehängt. Hier kann auch der Schriftzug "Solvanta" wegfallen und nur das Ankerstern genutzt werden.

```html
<!DOCTYPE html>
<html lang="de">
<head>
<meta charset="utf-8">
<title>Mutig voran – Plakat</title>
<link rel="stylesheet" href="https://fonts.googleapis.com/css2?family=Alfa+Slab+One&family=Arimo:wght@400;500&display=swap">
<style>
  :root {
    --red: #ad0b07;
    --white: #ffffff;
    --sky: #b9d4ee;
    --sky-light: #dde9f4;
    --meadow: #c9d3bf;
    --footer-text: #3a3a3a;
    --logo-blue: #1a9fe0;
  }
  html, body {
    margin: 0;
    padding: 0;
    width: 848px;
    height: 1200px;
    overflow: hidden;
    background: var(--white);
  }
  .poster {
    position: relative;
    width: 848px;
    height: 1200px;
    overflow: hidden;
    font-family: "Arimo", Arial, sans-serif;
  }
  .hero-photo {
    position: absolute;
    left: 0; top: 0;
    width: 848px; height: 1037px;
    background: linear-gradient(180deg, var(--sky) 0%, var(--sky-light) 60%, var(--meadow) 100%);
  }
  .headline {
    position: absolute;
    left: 54px; top: 40px;
    margin: 0;
    font-family: "Alfa Slab One", Georgia, serif;
    font-weight: 400;
    font-size: 122px;
    line-height: 114px;
    color: var(--red);
    letter-spacing: 1px;
  }
  .offer-badge {
    position: absolute;
    left: -17px; top: 612px;
    width: 448px; height: 448px;
    border-radius: 50%;
    background: var(--red);
    z-index: 2;
  }
  .offer-badge::before {
    content: "";
    position: absolute;
    inset: 13px;
    border: 2px solid var(--white);
    border-radius: 50%;
  }
  .offer-text {
    position: absolute;
    left: 0; top: 0;
    width: 448px;
    color: var(--white);
    text-align: center;
    font-size: 28px;
    line-height: 33px;
  }
  .offer-intro { position: absolute; top: 91px; left: 0; width: 100%; margin: 0; }
  .offer-rule {
    position: absolute;
    top: 220px; left: 142px;
    width: 163px; height: 3px;
    background: var(--white);
  }
  .offer-contact { position: absolute; top: 255px; left: 0; width: 100%; margin: 0; }
  .phone-icon { width: 22px; height: 22px; vertical-align: -2px; margin-right: 10px; }
  .footer-rule {
    position: absolute;
    left: 0; top: 1037px;
    width: 848px; height: 5px;
    background: var(--red);
  }
  .footer {
    position: absolute;
    left: 0; top: 1042px;
    width: 848px; height: 158px;
    background: var(--white);
  }
  .partner-solvanta {
    position: absolute;
    left: 42px; top: 46px;
    display: flex; align-items: center; gap: 10px;
    font-size: 22px;
    font-weight: 500;
    color: var(--logo-blue);
  }
  .partner-solvanta .mark {
    width: 46px; height: 46px;
    background: var(--logo-blue);
  }
  .org-name {
    position: absolute;
    right: 181px; top: 44px;
    margin: 0;
    text-align: right;
    font-size: 14.5px;
    line-height: 25px;
    color: var(--footer-text);
    letter-spacing: 0.3px;
  }
  .partner-vkm {
    position: absolute;
    left: 696px; top: 20px;
    width: 118px; height: 118px;
    border-radius: 50%;
    border: 3px solid var(--red);
    box-sizing: border-box;
    display: flex; align-items: center; justify-content: center;
    font-size: 30px;
    font-weight: 500;
    color: var(--red);
  }
</style>
</head>
<body>
<main class="poster">
  <div class="hero-photo" role="img" aria-label="Foto: schwangere Frau im hellen Sommerkleid vor blauem Himmel und Blumenwiese"></div>

  <h1 class="headline">Mutig<br>voran.</h1>

  <section class="offer-badge">
    <div class="offer-text">
      <p class="offer-intro">Wir begleiten Sie:<br>Vor, während und nach<br>Ihrer Schwangerschaft.</p>
      <div class="offer-rule"></div>
      <p class="offer-contact">Kontaktieren Sie uns:<br>
        <svg class="phone-icon" viewBox="0 0 24 24" aria-hidden="true"><path fill="#ffffff" d="M6.6 10.8c1.4 2.8 3.8 5.1 6.6 6.6l2.2-2.2c.3-.3.7-.4 1-.2 1.1.4 2.3.6 3.6.6.6 0 1 .4 1 1V20c0 .6-.4 1-1 1C10.6 21 3 13.4 3 4c0-.6.4-1 1-1h3.5c.6 0 1 .4 1 1 0 1.3.2 2.5.6 3.6.1.3 0 .7-.2 1l-2.3 2.2z"/></svg>0987/654321<br>oder<br>info@vkm-ev.de</p>
    </div>
  </section>

  <div class="footer-rule"></div>
  <footer class="footer">
    <div class="partner-solvanta"><span class="mark"></span>Solvanta</div>
    <p class="org-name">NACHBARSCHAFTSBUND<br>FÜR OFFENE WEGE e.V.<br>MARBURG</p>
    <div class="partner-vkm">VKM</div>
  </footer>
</main>
</body>
</html>
```